Business Card and Stationary
Small management consulting firm
Professional
Dwight Parmelee
President
5142 Heron Loop
Dunmore Crossing, VA 22817
dwight.parmelee@lw-advis.com
http://www.lw-advis.com
Our audience will be industry members of the defense consulting world as well as the US Government so we will need something memorable, but nothing too over the top.
Our Logo,
The slogan: "Real Strategy, Meaningful Change"
Our website: www.lw-advis.com
Here is the second design with our logo on the side

```html
<!DOCTYPE html>
<html lang="en">
<head>
<meta charset="utf-8">
<title>Lodgewood Advisory — Business Card</title>
<link rel="stylesheet" href="https://fonts.googleapis.com/css2?family=Tinos:wght@400;700&family=Open+Sans:wght@600;700&display=swap">
<style>
  :root {
    --page-bg: #e9e7e4;
    --card-white: #ffffff;
    --navy: #1f3f7a;
    --blue-top: #3f6fb3;
    --blue-bottom: #234e93;
    --accent-red: #b3161f;
    --accent-red-dark: #7e0d14;
    --logo-blue: #1e4a8c;
    --text-light: #ffffff;
    --text-soft: #e4ecf7;
    --divider: rgba(255,255,255,0.55);
  }
  * { margin: 0; padding: 0; box-sizing: border-box; }
  html, body {
    width: 1200px; height: 780px; overflow: hidden;
    background: var(--page-bg);
  }
  .canvas {
    position: relative; width: 1200px; height: 780px;
  }
  .card {
    position: absolute; left: 75px; top: 90px;
    width: 1050px; height: 600px;
    border-radius: 38px; overflow: hidden;
    background: var(--card-white);
    box-shadow: 0 14px 40px rgba(0,0,0,0.18);
  }
  .card-bands { position: absolute; inset: 0; width: 100%; height: 100%; }

  .brand {
    position: absolute; left: 215px; top: 92px;
    display: flex; align-items: center; gap: 28px;
  }
  .brand-dot {
    width: 118px; height: 118px; border-radius: 50%;
    background: var(--logo-blue);
  }
  .brand-name {
    font-family: "Tinos", serif; font-weight: 400;
    color: var(--logo-blue);
    text-transform: uppercase; letter-spacing: 1px;
    font-size: 50px; line-height: 1.05; text-align: center;
  }
  .brand-name .brand-suffix { display: block; font-size: 28px; letter-spacing: 4px; }

  .person {
    position: absolute; right: 545px; top: 362px;
    text-align: right; color: var(--text-light);
  }
  .person-name {
    font-family: "Open Sans", sans-serif; font-weight: 700;
    font-size: 30px; line-height: 1.1;
  }
  .person-title {
    font-family: "Open Sans", sans-serif; font-weight: 600;
    font-size: 19px; margin-top: 4px;
  }
  .person-address {
    font-family: "Tinos", serif; font-size: 24px; line-height: 1.3;
    margin-top: 26px; color: var(--text-soft);
  }

  .divider {
    position: absolute; left: 528px; top: 350px;
    width: 2px; height: 200px; background: var(--divider);
  }

  .contacts {
    position: absolute; left: 552px; top: 358px;
    list-style: none;
    font-family: "Tinos", serif; font-size: 23px; color: var(--text-soft);
  }
  .contacts li {
    display: flex; align-items: center; gap: 14px; height: 44px;
  }
  .contacts svg { width: 22px; height: 22px; flex: none; }
</style>
</head>
<body>
<div class="canvas">
  <div class="card">
    <svg class="card-bands" viewBox="0 0 1050 600" preserveAspectRatio="none" aria-hidden="true">
      <defs>
        <linearGradient id="blueBand" x1="0" y1="0" x2="0" y2="1">
          <stop offset="0" stop-color="var(--blue-top)"/>
          <stop offset="1" stop-color="var(--blue-bottom)"/>
        </linearGradient>
        <linearGradient id="redBand" x1="0" y1="0" x2="1" y2="0">
          <stop offset="0" stop-color="var(--accent-red-dark)"/>
          <stop offset="0.5" stop-color="var(--accent-red)"/>
          <stop offset="1" stop-color="var(--accent-red-dark)"/>
        </linearGradient>
      </defs>
      <path d="M0 318 C260 292 420 338 640 282 C820 236 960 216 1050 206 L1050 600 L0 600 Z" fill="#d9dde4"/>
      <path d="M0 326 C260 300 420 346 640 290 C820 244 960 224 1050 214 L1050 600 L0 600 Z" fill="url(#redBand)"/>
      <path d="M0 350 C260 328 430 372 650 312 C830 264 960 246 1050 238 L1050 600 L0 600 Z" fill="url(#blueBand)"/>
    </svg>

    <div class="brand">
      <div class="brand-dot"></div>
      <div class="brand-name">Lodgewood Advisory,<span class="brand-suffix">LLC</span></div>
    </div>

    <div class="person">
      <div class="person-name">Dwight Parmelee</div>
      <div class="person-title">President</div>
      <div class="person-address">5142 Heron Loop<br>Dunmore Crossing, VA 22817</div>
    </div>

    <div class="divider"></div>

    <ul class="contacts">
      <li>
        <svg viewBox="0 0 24 24" aria-label="Phone"><path fill="#fff" d="M6.6 10.8a15 15 0 0 0 6.6 6.6l2.2-2.2a1 1 0 0 1 1-.25 11.4 11.4 0 0 0 3.6.57 1 1 0 0 1 1 1V20a1 1 0 0 1-1 1A17 17 0 0 1 3 4a1 1 0 0 1 1-1h3.5a1 1 0 0 1 1 1c0 1.25.2 2.45.57 3.57a1 1 0 0 1-.25 1z"/></svg>
        540-318-2264
      </li>
      <li>
        <svg viewBox="0 0 24 24" aria-label="Fax"><path fill="#fff" d="M7 3h10v5H7zM4 9h16a2 2 0 0 1 2 2v6h-4v4H6v-4H2v-6a2 2 0 0 1 2-2zm4 7v3h8v-3z"/></svg>
        540-318-2290
      </li>
      <li>
        <svg viewBox="0 0 24 24" aria-label="Email"><circle cx="12" cy="12" r="9.5" fill="none" stroke="#fff" stroke-width="2"/><text x="12" y="16.5" text-anchor="middle" font-size="13" font-family="Arial, sans-serif" font-weight="700" fill="#fff">@</text></svg>
        dwight.parmelee@lw-advis.com
      </li>
      <li>
        <svg viewBox="0 0 24 24" aria-label="Website"><g fill="none" stroke="#fff" stroke-width="1.8"><circle cx="12" cy="12" r="9.5"/><ellipse cx="12" cy="12" rx="4" ry="9.5"/><path d="M2.5 12h19M4 7h16M4 17h16"/></g></svg>
        www.lw-advis.com
      </li>
    </ul>
  </div>
</div>
</body>
</html>
```